Business Card Design

Need a new business card to represent our legal vertical focus. attached is an example of our old business card and newest logo. we would like the card to also identify "Legal Tech" as a tag line of business.

Our new address is
4170 Marlowe Brook Rd.
Suite 518
Cincinnati, OH 45917

we no longer have a fax number.

Target Market(s)

Tech Consulting for Law Firms

Industry/Entity Type

Legal

Contact Information for Business Card

should use logo and colors. we are a b2b company

Other font styles liked:
• tahoma

Requirements
Must have
• all print should be in lower case just as shown in photos. tag line should not
Should not have
• pinstripes or drop shadows

```html
<!DOCTYPE html>
<html lang="en">
<head>
<meta charset="utf-8">
<title>Tandemark Legal Tech – Business Card</title>
<link href="https://fonts.googleapis.com/css2?family=Lato:wght@400;700&display=swap" rel="stylesheet">
<style>
  :root {
    --backdrop: #3a332f;
    --card: #1b1b1b;
    --card-edge: #141414;
    --ink: #f2f2f2;
    --muted: #a9a9a9;
    --accent: #f0542a;
  }
  * { margin: 0; padding: 0; box-sizing: border-box; }
  html, body {
    width: 1200px; height: 844px; overflow: hidden;
    background: var(--backdrop);
    font-family: "Lato", "Tahoma", sans-serif;
  }
  .sheet {
    position: relative; width: 1200px; height: 844px;
    display: flex; align-items: center; justify-content: center; gap: 50px;
  }
  .card {
    position: relative; width: 500px; height: 286px;
    background: var(--card);
    border: 1px solid var(--card-edge);
  }
  /* contact side */
  .card-front .mark-block {
    position: absolute; left: 92px; top: 103px;
    width: 80px; height: 80px; background: var(--accent);
  }
  .card-front .details {
    position: absolute; left: 238px; top: 70px; right: 16px; color: var(--ink);
  }
  .person-name { font-size: 21px; font-weight: 400; line-height: 1.1; }
  .person-role { font-size: 13px; color: var(--accent); margin-bottom: 12px; }
  .address { font-size: 14px; line-height: 1.35; margin-bottom: 12px; }
  .contact-list { list-style: none; font-size: 14px; line-height: 1.35; }
  .contact-list .label { color: var(--accent); display: inline-block; width: 22px; }
  /* logo side */
  .card-back .brand {
    position: absolute; left: 100px; top: 104px;
  }
  .brand-name {
    font-size: 46px; font-weight: 700; color: var(--ink); line-height: 1;
    display: flex; align-items: center; gap: 12px;
  }
  .brand-square { width: 22px; height: 22px; background: var(--ink); }
  .brand-tagline {
    font-size: 15px; color: var(--muted); text-align: right; margin-top: 2px;
  }
</style>
</head>
<body>
<main class="sheet">
  <section class="card card-front">
    <div class="mark-block" aria-hidden="true"></div>
    <div class="details">
      <p class="person-name">martin kessler</p>
      <p class="person-role">managingdirector</p>
      <p class="address">4170 marlowe brook rd., suite 518<br>cincinnati, oh 45917.</p>
      <ul class="contact-list">
        <li><span class="label">t:</span>044-555 018 246</li>
        <li><span class="label">e:</span>info@tandemark.com</li>
        <li><span class="label">w:</span>www.tandemark.com</li>
      </ul>
    </div>
  </section>
  <section class="card card-back">
    <div class="brand">
      <p class="brand-name"><span class="brand-square" aria-hidden="true"></span>Tandemark</p>
      <p class="brand-tagline">Legal Tech</p>
    </div>
  </section>
</main>
</body>
</html>
```